Looking for a dynamic business card for a pizzeria.

A business card with our food, logo, and space for name, title, email, website, phone. The card should convey quality, unique, amazing. On the front, I envision food photo or photos with the owners names and contact information. On the back, more food with locations, website, facebook, twitter, instagram icons. It should look polished, not cartoonish, or plain.
Target Market(s)
upscale, local food buyers, 30-50 years in age.
Industry/Entity Type
Restaurant
Contact Information for Business Card
Business Name: Crustella, LLC
Website: www.crustellaovens.com
Back:
2 locations: (can list on the back of card)
1. Harbor Row
2736 Marlow Street
Westbrook, WA 98301
360-555-0143
2. Linden Hill
1187 Pelham Street
Westbrook, WA 98304
360-555-0187
front:
EDITABLE space for
Business name
Person's Name
title
2nd title
Email address
cell-phone number
Requirements
Must have
- logo
- my food photo or photos (no watermarks showing)
- locations on back
- Person contact information on front
- full bleed

```html
<!DOCTYPE html>
<html lang="en">
<head>
<meta charset="utf-8">
<title>Crustella Business Card</title>
<link rel="stylesheet" href="https://fonts.googleapis.com/css2?family=Open+Sans:wght@400;600;700&display=swap">
<style>
  :root {
    --stage: #e9e6e1;
    --card: #ffffff;
    --ink: #2b2b2b;
    --ink-soft: #6b6b6b;
    --brand-green: #3f7d4e;
    --brand-red: #c8392e;
    --shadow: rgba(0,0,0,0.18);
  }
  html, body {
    margin: 0;
    padding: 0;
    width: 1200px;
    height: 900px;
    overflow: hidden;
    background: var(--stage);
    font-family: "Open Sans", sans-serif;
    color: var(--ink);
  }
  .canvas {
    width: 1200px;
    height: 900px;
    display: flex;
    flex-direction: column;
    align-items: center;
    justify-content: center;
    gap: 40px;
  }
  .card {
    position: relative;
    width: 700px;
    height: 400px;
    background: var(--card);
    box-shadow: 0 6px 18px var(--shadow);
    overflow: hidden;
  }

  /* Back: locations and food */
  .locations {
    position: absolute;
    left: 48px;
    top: 58px;
    font-size: 17px;
    line-height: 1.4;
  }
  .location { margin-bottom: 18px; }
  .location-name { font-weight: 700; font-size: 19px; }
  .food-gallery {
    position: absolute;
    right: 0;
    top: 0;
    width: 400px;
    height: 400px;
  }

  /* Front: contact and brand */
  .contact {
    position: absolute;
    left: 48px;
    top: 118px;
    font-size: 15px;
    line-height: 1.65;
    color: var(--ink-soft);
  }
  .contact-name { font-weight: 600; color: var(--ink); }
  .brand {
    position: absolute;
    right: 60px;
    top: 160px;
    display: flex;
    align-items: center;
    gap: 16px;
  }
  .brand-name {
    font-size: 52px;
    font-weight: 700;
    color: var(--brand-green);
    letter-spacing: 1px;
  }
  .brand-dot {
    width: 56px;
    height: 56px;
    border-radius: 50%;
    background: var(--brand-red);
  }
</style>
</head>
<body>
<main class="canvas">

  <section class="card card-back">
    <div class="locations">
      <div class="location">
        <div class="location-name">Harbor Row</div>
        <div>2736 Marlow Street</div>
        <div>Westbrook, WA 98301</div>
        <div>360-555-0143</div>
      </div>
      <div class="location">
        <div class="location-name">Linden Hill</div>
        <div>1187 Pelham Street</div>
        <div>Westbrook, WA 98304</div>
        <div>360-555-0187</div>
      </div>
    </div>
    <svg class="food-gallery" viewBox="0 0 400 400" xmlns="http://www.w3.org/2000/svg">
      <defs>
        <radialGradient id="meat-tone"><stop offset="0" stop-color="#e3a198"/><stop offset="1" stop-color="#b5655c"/></radialGradient>
        <radialGradient id="bread-tone"><stop offset="0" stop-color="#ecd3b2"/><stop offset="1" stop-color="#c49a6c"/></radialGradient>
        <radialGradient id="greens-tone"><stop offset="0" stop-color="#d8c56a"/><stop offset="1" stop-color="#7d9c4c"/></radialGradient>
        <radialGradient id="sauce-tone"><stop offset="0" stop-color="#e9935f"/><stop offset="1" stop-color="#b8502f"/></radialGradient>
      </defs>
      <circle role="img" aria-label="Photo of sliced cured meats" cx="150" cy="105" r="80" fill="url(#meat-tone)" stroke="#fff" stroke-width="6"/>
      <circle role="img" aria-label="Photo of fresh baked bread" cx="302" cy="140" r="78" fill="url(#bread-tone)" stroke="#fff" stroke-width="6"/>
      <circle role="img" aria-label="Photo of a sandwich with salad" cx="140" cy="275" r="80" fill="url(#greens-tone)" stroke="#fff" stroke-width="6"/>
      <circle role="img" aria-label="Photo of a pizza fresh from the oven" cx="295" cy="300" r="82" fill="url(#sauce-tone)" stroke="#fff" stroke-width="6"/>
    </svg>
  </section>

  <section class="card card-front">
    <div class="contact">
      <div class="contact-name">Jonah Ferrante, Owner</div>
      <div>Managing Partner</div>
      <div>jonah@crustellaovens.com</div>
      <div>360-555-0112</div>
      <div>cell 360-555-0168</div>
      <div>www.crustellaovens.com</div>
    </div>
    <div class="brand">
      <span class="brand-name">Crustella</span>
      <span class="brand-dot"></span>
    </div>
  </section>

</main>
</body>
</html>
```